VELMAR WEBSITE

need to create a new website for VELMAR ltd
the company deals with all aspects of safety products & safety wear
we need a simple website to show
ideas can be taken from following website whose products we shall distribute in kenya
www.qtw.co.uk
www.brovik.eu
www.tormanhardgear.com
www.qalvenworks.co.za

we need following tabs
1) home - basic company information
2) products - broken down to following categories ie gloves, head protection, ear protection, mouth protection, foot protection
3) contacts

the company profile is a reputable company dealing with all aspects of safety, HSE (health and safety equipment), and PPE (personal protective equipment)

the website should have the brovik logo for which we are an authorized distributor.
the brovi industrial range writeup can be picked from their website

Dear Designers, i shall be able to choose a final design in 2 weeks, sorry i have not been able to finalise this due to a personal reason

Target Market(s)

the buyers are all types of industry who care for their employees safety

Industry/Entity Type

Industrial

Requirements
Must have
• clean look, fresh look, user freindly
Nice to have
• clear images, quick links etc

```html
<!DOCTYPE html>
<html lang="en">
<head>
<meta charset="utf-8">
<title>VELMAR – Safety Products &amp; Safety Wear</title>
<link rel="stylesheet" href="https://fonts.googleapis.com/css2?family=Open+Sans:wght@300;400;600&display=swap">
<style>
:root{
  --navy:#0f2e3b;
  --navy-dark:#0b2430;
  --gold:#f5b800;
  --orange:#d98a1c;
  --text:#7a7a7a;
  --text-dark:#333;
  --title:#16313d;
  --muted:#9a9a9a;
  --line:#d8d8d8;
  --panel:#f7f7f7;
  --footer:#222;
}
*{box-sizing:border-box;margin:0;padding:0}
html,body{width:1070px;height:1200px;overflow:hidden;background:#fff;font-family:"Open Sans",Arial,sans-serif;color:var(--text)}
.page{position:relative;width:1070px;height:1200px}
.abs{position:absolute}

/* header */
.site-header{position:absolute;left:0;top:0;width:1070px;height:117px;background:linear-gradient(#fff,#f2f2f2);border-bottom:1px solid #e4e4e4}
.brand{position:absolute;left:104px;top:38px;display:flex;align-items:center;gap:8px;font-weight:600;font-size:27px;color:var(--navy);letter-spacing:1px}
.brand-mark{width:20px;height:20px;background:var(--gold)}
.phone{position:absolute;left:658px;top:22px;font-size:18px;font-weight:300;color:var(--title)}
.search{position:absolute;left:801px;top:20px;width:167px;height:29px;border:1px solid #cfcfcf;border-radius:4px;background:#fff}
.search span{position:absolute;left:9px;top:6px;font-size:11px;color:#bbb}
.search .divider{position:absolute;left:134px;top:6px;width:1px;height:17px;background:#ddd}
.search svg{position:absolute;left:141px;top:6px}
.main-nav{position:absolute;left:299px;top:73px;height:25px;font-size:11.5px;color:#5a6a72}
.main-nav a{position:absolute;top:5px;white-space:nowrap;text-decoration:none;color:inherit}
.main-nav a.active{top:0;left:0;width:54px;height:25px;background:var(--navy);color:#fff;font-size:12px;text-align:center;line-height:25px;border-radius:2px}

/* hero */
.hero{position:absolute;left:0;top:119px}
.slider-arrow{position:absolute;background:var(--navy)}

/* features */
.feature{position:absolute;top:490px;width:268px}
.feature h2{font-size:16.5px;font-weight:400;color:#6e6e6e;margin-left:6px}
.feature h2.current{color:var(--title)}
.feature .thumb{margin-top:16px;height:70px}
.feature p{margin-top:14px;font-size:11.3px;line-height:17.9px;color:var(--text)}
.read-more{display:flex;align-items:center;gap:3px;font-size:10px;color:#aaa;margin-top:8px}
.read-more i{display:block;width:10px;height:10px;background:#2a6a6a;position:relative}
.read-more i::before,.read-more i::after{content:"";position:absolute;background:#fff}
.read-more i::before{left:2px;top:4px;width:6px;height:2px}
.read-more i::after{left:4px;top:2px;width:2px;height:6px}

/* news */
.news{position:absolute;left:110px;top:812px;width:262px;height:314px;background:var(--panel);border:1px solid #e3e3e3;border-radius:3px}
.news h3{position:absolute;left:14px;top:16px;font-size:21px;font-weight:300;color:var(--title)}
.news h3 b{font-weight:400}
.dots{position:absolute;left:198px;top:27px;display:flex;gap:3px}
.dots span{width:8px;height:8px;border-radius:50%;background:var(--gold)}
.dots span:first-child{background:var(--navy)}
.news .rule{position:absolute;left:14px;top:51px;width:234px;border-top:1px dashed #c8c8c8}
.news-item{position:absolute;left:13px;width:240px}
.news-item .avatar{position:absolute;left:0;top:0;width:70px;height:63px}
.news-item h4{position:absolute;left:76px;top:-2px;font-size:12.5px;font-weight:400;color:var(--text-dark)}
.news-item p{position:absolute;left:76px;top:17px;width:150px;font-size:10.3px;line-height:12.7px;color:var(--muted)}

/* about */
.about{position:absolute;left:393px;top:812px;width:568px;height:312px;background:#fff;border:3px solid #eee}
.about h3{position:absolute;left:33px;top:18px;font-size:21px;font-weight:300;color:var(--title)}
.about .rule{position:absolute;left:33px;top:55px;width:507px;border-top:1px dashed #c8c8c8}
.about p{position:absolute;left:33px;width:525px;font-size:12.4px;line-height:17.6px;font-weight:300;color:#555}
.btn{position:absolute;left:34px;top:261px;width:99px;height:29px;background:var(--navy);color:#fff;font-size:12.5px;line-height:29px;text-align:center;border-radius:2px}

/* footer */
.site-footer{position:absolute;left:0;top:1152px;width:1070px;height:48px;background:var(--footer);color:#ddd;font-size:11.8px;text-align:center;line-height:48px}
</style>
</head>
<body>
<div class="page">

  <header class="site-header">
    <div class="brand"><span class="brand-mark"></span>VELMAR</div>
    <div class="phone">(800) 555-0142</div>
    <div class="search">
      <span>Search</span>
      <div class="divider"></div>
      <svg width="17" height="17" viewBox="0 0 17 17"><circle cx="7" cy="7" r="5" fill="none" stroke="#666" stroke-width="2"/><line x1="11" y1="11" x2="15" y2="15" stroke="#666" stroke-width="2.4" stroke-linecap="round"/></svg>
    </div>
    <nav class="main-nav">
      <a class="active" href="#">HOME</a>
      <a href="#" style="left:69px">Head Protection</a>
      <a href="#" style="left:178px">Ear Protection</a>
      <a href="#" style="left:276px">Mouth Protection</a>
      <a href="#" style="left:392px">Foot Protection</a>
      <a href="#" style="left:497px">HS Equipment</a>
      <a href="#" style="left:598px">PP Equipment</a>
    </nav>
  </header>

  <svg class="hero" width="1070" height="346" viewBox="0 0 1070 346" role="img" aria-label="Slide photo: worker in blue overalls wearing ear defenders and safety glasses at an industrial machine">
    <defs>
      <linearGradient id="heroFill" x1="0" y1="0" x2="1" y2="0.4">
        <stop offset="0" stop-color="#d9d4cc"/>
        <stop offset="0.3" stop-color="#3c5aa8"/>
        <stop offset="0.55" stop-color="#8e8b86"/>
        <stop offset="0.8" stop-color="#b59b7c"/>
        <stop offset="1" stop-color="#6f6458"/>
      </linearGradient>
    </defs>
    <polygon points="169,0 999,0 883,345 56,345" fill="url(#heroFill)"/>
  </svg>

  <div class="slider-arrow" style="left:0;top:236px;width:49px;height:106px">
    <svg width="49" height="106" viewBox="0 0 49 106"><polyline points="29,38 18,53 29,68" fill="none" stroke="#fff" stroke-width="5"/></svg>
  </div>
  <div class="slider-arrow" style="left:1022px;top:236px;width:48px;height:110px">
    <svg width="48" height="110" viewBox="0 0 48 110"><polyline points="19,40 30,55 19,70" fill="none" stroke="#fff" stroke-width="5"/></svg>
  </div>

  <section class="feature" style="left:116px">
    <h2 class="current">Head Protection</h2>
    <div class="thumb" role="img" aria-label="Worker in blue hard hat in front of a steel structure" style="background:linear-gradient(90deg,#8fa3b5,#2f6fb5 30%,#c9d6e2 60%,#7fb0d8);border-bottom:2px solid var(--navy)"></div>
    <p>It is a long established fact that a reader will be distracted by the readable content of a page when looking at its layout. The point of using Lorem Ipsum is that it has a more-or-less normal distribution of letters, as opposed to using 'Con-tent here, content here', making it look like read-able English. Many desktop publishing packages</p>
    <div class="read-more" style="margin-top:1px"><i></i>read more</div>
  </section>

  <section class="feature" style="left:404px">
    <h2>Gloves Protection</h2>
    <div class="thumb" role="img" aria-label="Dark photo of safety boots" style="background:linear-gradient(90deg,#3a2c1c,#5a4126 50%,#2c2016);border-bottom:2px solid var(--orange)"></div>
    <p>It is a long established fact that a reader will be distracted by the readable content of a page when looking at its layout.<br>The point of using Lorem Ipsum is that it has a more-or-less normal distribution of letters, as</p>
    <div class="read-more" style="margin-top:12px"><i></i>read more</div>
  </section>

  <section class="feature" style="left:691px">
    <h2>ASK ORVEN</h2>
    <div class="thumb" role="img" aria-label="Dark photo of protective mouth guards on wood" style="background:linear-gradient(90deg,#3b2414,#54321b 50%,#3a2414);border-bottom:2px solid var(--orange)"></div>
    <p>It is a long established fact that a reader will be distracted by the readable content of a page when looking at its layout.<br>The point of using Lorem Ipsum is that it has a more-or-less normal distribution of letters, as opposed to using 'Content here, content here', making it look like readable English. Many desk-</p>
    <div class="read-more" style="margin-top:12px"><i></i>read more</div>
  </section>

  <aside class="news">
    <h3>Our <b>News</b></h3>
    <div class="dots"><span></span><span></span><span></span><span></span></div>
    <div class="rule"></div>
    <div class="news-item" style="top:65px">
      <div class="avatar" role="img" aria-label="Portrait photo" style="background:linear-gradient(#b9987e,#8a6a55)"></div>
      <h4>Lorem Lipsum</h4>
      <p>It is a long established fact that a reader will be distracted by the readable</p>
    </div>
    <div class="news-item" style="top:150px">
      <div class="avatar" role="img" aria-label="Portrait photo" style="background:linear-gradient(#e9e6e3,#4a3f45)"></div>
      <h4>Lorem Lipsum</h4>
      <p>It is a long established fact that a reader will be distracted by the readable</p>
    </div>
    <div class="news-item" style="top:236px">
      <div class="avatar" role="img" aria-label="Portrait photo" style="background:linear-gradient(#b9987e,#8a6a55)"></div>
      <h4>Lorem Lipsum</h4>
      <p>It is a long established fact that a reader will be distracted by the readable</p>
    </div>
  </aside>

  <section class="about">
    <h3>About Us</h3>
    <div class="rule"></div>
    <p style="top:73px">It is a long established fact that a reader will be distracted by the readable content of a page when looking at its layout. The point of using Lorem Ipsum is that it has a more-or-less normal distribution of letters, as opposed to using 'Content here, content here', making it look like readable English. Many desktop publishing packages and web page editors now use Lorem Ipsum as their default model text, and a search for 'lorem ipsum' will uncover many web sites still in their infancy. Various versions have evolved over the years, sometimes by accident, sometimes on purpose (injected humour and the like).</p>
    <p style="top:213px">It is a long established fact that a reader will be distracted by the readable content of a page when looking at its layout.</p>
    <a class="btn">Read More</a>
  </section>

  <footer class="site-footer">©2003 Velmar Protection, Inc. |&nbsp;&nbsp;&nbsp;All rights reserved.</footer>
</div>
</body>
</html>
```